Quill And Ferry Business Card

I need a business card designed around my logo (which was designed here on Sketch Forum!)

Target Market(s)

Professional Businesses

Industry/Entity Type

Business

Requirements
Must have
• Details that must be on the business card:

Renata Ovalle
Director
0491 253 608
renata@quillandferry.com.au
www.quillandferry.com.au
PO Box 4720 Fitzroy North Vic 3068

```html
<!DOCTYPE html>
<html lang="en">
<head>
<meta charset="utf-8">
<title>Quill And Ferry Business Card</title>
<link rel="stylesheet" href="https://fonts.googleapis.com/css2?family=PT+Sans:ital,wght@0,400;0,700;1,700&family=PT+Sans+Narrow:wght@400;700&display=swap">
<style>
  :root {
    --paper: #ffffff;
    --ink: #111111;
    --crop: #222222;
    --card-edge: #9a9a9a;
    --red-light: #e25555;
    --red-mid: #d42020;
    --red-deep: #b30a0a;
    --silver-light: #f4f5f5;
    --silver-mid: #dcdfdf;
    --silver-dark: #c4c8c8;
    --brand-ink: #1d1d1d;
  }
  * { margin: 0; padding: 0; box-sizing: border-box; }
  html, body {
    width: 979px; height: 1200px; overflow: hidden;
    background: var(--paper);
  }
  .sheet { position: relative; width: 979px; height: 1200px; }
  .crop-marks { position: absolute; inset: 0; }
  .card {
    position: absolute; left: 87px; width: 805px; height: 460px;
    border: 1px solid var(--card-edge); overflow: hidden;
  }
  .card--front {
    top: 83px;
    background: linear-gradient(160deg, var(--silver-light) 0%, var(--silver-mid) 45%, var(--silver-light) 70%, var(--silver-dark) 100%);
  }
  .card--back { top: 656px; background: var(--paper); }

  .droplet-field {
    position: absolute; left: 20px; top: 20px; width: 470px; height: 410px;
    border-radius: 50%;
    background: radial-gradient(ellipse at 45% 45%, rgba(255,255,255,0.95) 0%, rgba(255,255,255,0.6) 45%, rgba(255,255,255,0) 72%);
  }

  .brand {
    position: absolute; display: flex; align-items: center;
    font-family: "PT Sans Narrow", sans-serif; font-weight: 400;
    color: var(--brand-ink); text-transform: uppercase; white-space: nowrap;
  }
  .brand__mark { background: var(--red-mid); flex: none; }
  .brand--front { left: 130px; top: 172px; font-size: 62px; letter-spacing: 2px; }
  .brand--front .brand__mark { width: 58px; height: 58px; margin-right: 30px; }
  .brand--back { left: 385px; top: 82px; font-size: 38px; letter-spacing: 1px; }
  .brand--back .brand__mark { width: 36px; height: 36px; margin-right: 18px; }

  .red-panel { position: absolute; left: 0; top: 0; width: 805px; height: 460px; }

  .holder { font-family: "PT Sans", sans-serif; color: var(--paper); }
  .holder__line { position: absolute; text-align: right; white-space: nowrap; }
  .holder__name { right: 422px; top: 182px; font-weight: 700; font-size: 46px; line-height: 52px; }
  .holder__title, .holder__phone { font-weight: 700; font-style: italic; font-size: 29px; line-height: 32px; }
  .holder__title { right: 405px; top: 233px; }
  .holder__phone { right: 381px; top: 266px; }

  .contact {
    position: absolute; left: 424px; top: 194px;
    font-family: "PT Sans Narrow", sans-serif; font-size: 26px; line-height: 36px;
    color: var(--ink); list-style: none; white-space: nowrap;
  }
  .contact li:nth-child(2) { padding-left: 18px; }
  .contact li:nth-child(3) { padding-left: 34px; }
</style>
</head>
<body>
<div class="sheet">
  <svg class="crop-marks" width="979" height="1200" aria-hidden="true">
    <g stroke="var(--crop)" stroke-width="1">
      <line x1="87.5" y1="0" x2="87.5" y2="55"/>
      <line x1="891.5" y1="0" x2="891.5" y2="55"/>
      <line x1="87.5" y1="572" x2="87.5" y2="628"/>
      <line x1="891.5" y1="572" x2="891.5" y2="628"/>
      <line x1="87.5" y1="1145" x2="87.5" y2="1200"/>
      <line x1="891.5" y1="1145" x2="891.5" y2="1200"/>
      <line x1="0" y1="83.5" x2="57" y2="83.5"/>
      <line x1="920" y1="83.5" x2="979" y2="83.5"/>
      <line x1="0" y1="543.5" x2="57" y2="543.5"/>
      <line x1="920" y1="543.5" x2="979" y2="543.5"/>
      <line x1="0" y1="656.5" x2="57" y2="656.5"/>
      <line x1="920" y1="656.5" x2="979" y2="656.5"/>
      <line x1="0" y1="1116.5" x2="57" y2="1116.5"/>
      <line x1="920" y1="1116.5" x2="979" y2="1116.5"/>
    </g>
  </svg>

  <section class="card card--front">
    <div class="droplet-field" role="img" aria-label="Cluster of glossy white water droplets on brushed silver"></div>
    <div class="brand brand--front"><span class="brand__mark"></span>Quill And Ferry</div>
  </section>

  <section class="card card--back">
    <svg class="red-panel" width="805" height="460" aria-hidden="true">
      <defs>
        <linearGradient id="panelRed" x1="0" y1="0" x2="0.3" y2="1">
          <stop offset="0" stop-color="var(--red-light)"/>
          <stop offset="0.55" stop-color="var(--red-mid)"/>
          <stop offset="1" stop-color="var(--red-deep)"/>
        </linearGradient>
      </defs>
      <polygon points="0,0 298,0 533,460 0,460" fill="url(#panelRed)"/>
    </svg>
    <div class="brand brand--back"><span class="brand__mark"></span>Quill And Ferry</div>
    <div class="holder">
      <p class="holder__line holder__name">Renata Ovalle</p>
      <p class="holder__line holder__title">Director</p>
      <p class="holder__line holder__phone">0491 253 608</p>
    </div>
    <ul class="contact">
      <li>renata@quillandferry.com.au</li>
      <li>www.quillandferry.com.au</li>
      <li>PO Box 4720 Fitzroy North Vic 3068</li>
    </ul>
  </section>
</div>
</body>
</html>
```